Beauty Salon Design

The business card design will be for a new beauty salon opening up.

The therapist has over 11 years at a leading beauty Salon in perth.

The two colours that the salon will use is black and gold.

Industry/Entity Type

Beauty Salon

Contact Information for Business Card

Lumora Beauty

Corinne Halstead Pryce
Advanced beauty therapist
0455 817 302

Monday - Friday 9am - 2.30pm
Weekends and nights by appointment only

Waxing, Tinting, Swedish massage, hot stone massage, facials, peels, micro, LED light treatment, skin needling and retail products.

```html
<!DOCTYPE html>
<html lang="en">
<head>
<meta charset="utf-8">
<title>Lumora Beauty – Business Card</title>
<link rel="stylesheet" href="https://fonts.googleapis.com/css2?family=Questrial&display=swap">
<style>
  :root {
    --page: #ffffff;
    --card: #000000;
    --ivory: #f3f0e6;
    --gold: #c9a46a;
    --grey: #d9d9d9;
    --white: #ffffff;
    --skin-light: #b88a6e;
    --skin-mid: #6e4a38;
    --bronze: #a8743c;
  }
  * { margin: 0; padding: 0; box-sizing: border-box; }
  html, body {
    width: 1200px; height: 1000px; overflow: hidden;
    background: var(--page);
    font-family: "Questrial", "Century Gothic", sans-serif;
  }
  .card {
    position: absolute; left: 236px; width: 716px; height: 430px;
    background: var(--card); overflow: hidden;
  }
  .card--front { top: 60px; }
  .card--back { top: 518px; }

  .brand {
    position: absolute; left: 0; right: 0; top: 180px;
    display: flex; align-items: center; justify-content: center; gap: 18px;
  }
  .brand__dot {
    width: 34px; height: 34px; border-radius: 50%; background: var(--gold);
  }
  .brand__name {
    color: var(--ivory); font-size: 56px; letter-spacing: 1px; line-height: 1;
  }

  .portrait {
    position: absolute; left: 0; top: 0; width: 430px; height: 430px;
    background:
      radial-gradient(ellipse 55% 70% at 30% 60%, var(--skin-light) 0%, var(--skin-mid) 45%, rgba(0,0,0,0) 78%),
      radial-gradient(ellipse 40% 18% at 35% 18%, var(--bronze) 0%, rgba(0,0,0,0) 80%),
      var(--card);
  }

  .therapist {
    position: absolute; right: 48px; top: 56px; text-align: right;
  }
  .therapist__name { color: var(--grey); font-size: 23px; letter-spacing: 0.3px; }
  .therapist__title { color: var(--gold); font-size: 15px; margin-top: 2px; }

  .contact {
    position: absolute; right: 50px; top: 205px; text-align: right; color: var(--white);
  }
  .contact__phone {
    display: flex; align-items: center; justify-content: flex-end; gap: 8px;
    font-size: 16px; letter-spacing: 0.5px;
  }
  .contact__phone svg { width: 13px; height: 11px; }
  .contact__hours { font-size: 8px; margin-top: 3px; }

  .services {
    position: absolute; right: 48px; top: 345px; text-align: right;
    color: var(--white); font-size: 7.6px; line-height: 10px;
  }
</style>
</head>
<body>
  <section class="card card--front">
    <div class="brand">
      <span class="brand__dot"></span>
      <span class="brand__name">Lumora Beauty</span>
    </div>
  </section>

  <section class="card card--back">
    <div class="portrait" role="img" aria-label="Photograph: profile of a model with dramatic black and gold eye makeup and gold paint drips"></div>

    <div class="therapist">
      <p class="therapist__name">Corinne Halstead Pryce</p>
      <p class="therapist__title">Advanced Beauty Therapist</p>
    </div>

    <div class="contact">
      <p class="contact__phone">
        <svg viewBox="0 0 13 11" aria-hidden="true">
          <path d="M1 3.5 Q6.5 -0.5 12 3.5 L10.5 5 L8.5 3.8 L8.5 2.6 Q6.5 2 4.5 2.6 L4.5 3.8 L2.5 5 Z" fill="#fff"/>
          <path d="M3 6 L10 6 L11 10.5 L2 10.5 Z" fill="#fff"/>
        </svg>
        0455.817.302
      </p>
      <p class="contact__hours">Monday - Friday 9 AM - 2:30 PM</p>
    </div>

    <div class="services">
      <p>Weekends &amp; Nights by appointment</p>
      <p>Only waxing, tinting, swedish massage, hot stone massage, facials</p>
      <p>peels, micro, LED light treatment, skin needling and retail products</p>
    </div>
  </section>
</body>
</html>
```